Landing Page & Logo for Over 50s Guaranteed Life Cover

www.silveryearsquote.com provides a method of comparing guaranteed life cover for consumers aged over 50. The approach we are initially looking to deploy is a simple landing page that provides the user with high level information about SilverYearsQuote and allows them to see which provider is offering the best deal by ranking providers in a table. This will compare costs / core features in the same way as shown in the attached file.

The page should incorporate a new logo design for SilverYearsQuote.com which should be similar in design to the website goldenagepolicies.com.

Key elements of the landing page include:

Header (incorporating new logo and strapline e.g. "helping you find the best cover at the best price")
Introductory Text (to allow brief description of the service)
Comparison Table (to show top 10 providers - to include logos)
Table Links (allows customer to link directly from the table to the providers site)
Helpline (details of helpline number 0800 731 2946 - not actual number)
Join The Club (allows customers to sign up - using their email - to the over 50s club for more information and offers)

Other design elements welcomed to ensure the landing page is simple to understand, easy to navigate, visually appealing, focused on driving action / sales.
Updates

Additional payment approx. £60 for incorporating a new logo. Added Monday, April 25, 2016

Target Market(s)

50 - 80

Industry/Entity Type

Insurance

Logo Text

silveryearsquote and strapline "helping you find the best cover at the best price"

Number of Pages Required

1 page

Font styles to use
Sans Serif

Colors
a5ce39
add136
cadf82
eaf2ce
ffffff

Requirements
Nice to have
• Ideally created so content can be managed via WordPress.

```html
<!DOCTYPE html>
<html lang="en">
<head>
<meta charset="utf-8">
<title>SilverYearsQuote – Over 50s Life Cover</title>
<link rel="stylesheet" href="https://fonts.googleapis.com/css2?family=Raleway:wght@400;500;600&family=Open+Sans:wght@400;600;700&display=swap">
<style>
:root{
  --green:#a5ce39;
  --green-2:#add136;
  --green-dark:#6aaa1e;
  --green-btn:#72b21c;
  --green-soft:#cadf82;
  --green-pale:#eaf2ce;
  --white:#ffffff;
  --ink:#222222;
  --text:#666666;
  --muted:#a0a0a0;
  --line:#e2e2e2;
  --grey-bg:#f3f3f3;
  --table-head:#5a5a5a;
  --dark:#2f3133;
}
*{box-sizing:border-box;margin:0;padding:0}
html,body{width:1200px;height:2528px;overflow:hidden;background:var(--white)}
body{position:relative;font-family:'Open Sans',sans-serif;color:var(--text)}
.abs{position:absolute}

/* header */
.site-header{position:absolute;left:0;top:0;width:1200px;height:131px}
.brand{position:absolute;left:180px;top:38px;display:flex;align-items:center;gap:12px}
.brand-dot{width:34px;height:34px;border-radius:50%;background:var(--green)}
.brand-name{font-family:'Raleway',sans-serif;font-weight:500;font-size:34px;color:#3a3a3a;line-height:1}
.brand-tag{position:absolute;left:226px;top:92px;font-family:'Raleway',sans-serif;font-size:14px;color:#555}
.helpline{position:absolute;left:851px;top:62px}
.helpline-label{font-size:14px;color:var(--green-dark);font-family:'Raleway',sans-serif}
.helpline-number{display:flex;align-items:center;gap:6px;font-size:21px;color:#111;margin-top:4px}

/* nav */
.main-nav{position:absolute;left:0;top:131px;width:1200px;height:51px;background:linear-gradient(#9fd24a,#72b52a)}
.main-nav ul{list-style:none;position:absolute;left:180px;top:0;display:flex;height:51px}
.main-nav li{font-family:'Raleway',sans-serif;font-weight:500;font-size:14px;color:var(--white);padding:0 26px;line-height:51px;letter-spacing:.3px}
.main-nav li.active{background:#0d0d0d;padding:0 36px}

/* hero */
.hero{position:absolute;left:0;top:182px;width:1200px;height:472px;overflow:hidden}
.hero-photo{position:absolute;inset:0;background:radial-gradient(ellipse at 55% 25%,#fff5b0 0%,#e7d94d 25%,#a8b526 55%,#5f6e18 100%)}
.hero-curve{position:absolute;left:0;bottom:0}
.hero-title{position:absolute;left:0;width:1200px;top:134px;text-align:center;font-family:'Raleway',sans-serif;font-weight:500;font-size:37px;color:#111;letter-spacing:.5px}
.hero-sub{position:absolute;left:0;width:1200px;top:184px;text-align:center;font-family:'Raleway',sans-serif;font-weight:500;font-size:24px;color:#111}
.hero-btn{position:absolute;left:537px;top:230px;width:126px;height:35px;background:var(--green-btn);color:var(--white);font-size:13px;text-align:center;line-height:35px}
.hero-dots{position:absolute;left:566px;top:398px;display:flex;gap:4px}
.hero-dots span{width:13px;height:13px;border-radius:50%;background:var(--white);opacity:.85}
.hero-dots span:last-child{background:transparent;border:2px solid var(--white)}
.hero-arrow{position:absolute;top:160px;width:32px;height:32px;background:rgba(255,255,255,.35)}

/* about */
.about-title{position:absolute;left:0;width:1200px;top:656px;text-align:center;font-family:'Raleway',sans-serif;font-size:30px;color:#333}
.about-text{position:absolute;left:230px;width:740px;top:712px;text-align:center;font-size:12.5px;line-height:26px;color:#666}
.btn-outline{position:absolute;left:537px;top:807px;width:139px;height:37px;border:2px solid #d6d6d6;font-family:'Raleway',sans-serif;font-weight:500;font-size:14px;color:#444;text-align:center;line-height:33px}

/* product hexes */
.products{position:absolute;left:188px;top:893px;display:flex;gap:0}
.product{position:relative;width:207px;height:240px}
.product svg.hex{position:absolute;left:0;top:0}
.product-icon{position:absolute;left:74px;top:36px;width:60px;height:56px;border-radius:10px;background:var(--green-btn)}
.product-name{position:absolute;left:0;width:207px;top:112px;text-align:center;font-family:'Raleway',sans-serif;font-weight:500;font-size:16px;color:#333}
.product-hint{position:absolute;left:0;width:207px;top:138px;text-align:center;font-size:11px;color:#aaa}
.product-btn{position:absolute;left:55px;top:163px;width:97px;height:29px;border-radius:15px;background:var(--green-btn);color:var(--white);font-size:11px;text-align:center;line-height:29px}
.carousel-arrow{position:absolute;top:990px;width:30px;height:38px;background:#e6e6e6;border-radius:50%}

/* comparison */
.comparison{position:absolute;left:0;top:1230px;width:1200px;height:763px;background:linear-gradient(135deg,#f7f7f7,#ececec 50%,#f6f6f6)}
.comparison-title{position:absolute;left:0;width:1200px;top:40px;text-align:center;font-family:'Raleway',sans-serif;font-size:23px;color:#333}
.compare-table{position:absolute;left:234px;top:101px;width:730px;border-collapse:collapse;background:var(--white);table-layout:fixed}
.compare-table th{height:39px;background:var(--table-head);color:var(--white);font-weight:600;font-size:11px}
.compare-table td{height:76px;border-bottom:2px solid var(--line);text-align:center;vertical-align:top;padding-top:16px;font-size:12px;color:#555}
.compare-table td.provider{vertical-align:middle;padding-top:0;font-weight:700;font-size:15px}
.compare-table td.amount{font-size:14px;color:#333}
.info{display:block;margin:5px auto 0;width:17px;height:17px;border-radius:50%;background:#a9a9a9;color:var(--white);font-size:11px;font-weight:700;line-height:17px;font-family:Georgia,serif}
.buy{display:block;margin:0 auto;width:74px;height:22px;background:var(--green-btn);color:var(--white);font-size:9px;font-weight:700;line-height:22px}
.more{display:block;margin:5px auto 0;width:74px;height:22px;border:1px solid #cfcfcf;color:#777;font-size:8px;line-height:20px}
.compare-table td.buycol{padding-top:10px}

/* club */
.club{position:absolute;left:0;top:1993px;width:1200px;height:258px;overflow:hidden}
.club-photo{position:absolute;inset:0;background:linear-gradient(110deg,#3d3f41,#6c6e70 45%,#55575a 70%,#2c2e30)}
.club-title{position:absolute;left:0;width:1200px;top:46px;text-align:center;font-family:'Raleway',sans-serif;font-size:28px;color:var(--white)}
.club-text{position:absolute;left:260px;width:680px;top:84px;text-align:center;font-size:14px;line-height:27px;color:#f0f0f0}
.signup{position:absolute;left:399px;top:155px;width:374px;height:38px;background:var(--white);border:2px solid #111;display:flex}
.signup-field{flex:1;font-size:12px;color:#aaa;padding-left:40px;line-height:34px}
.signup-btn{width:92px;background:#0d0d0d;color:var(--white);font-size:12px;font-weight:700;text-align:center;line-height:34px}

/* footer */
.site-footer{position:absolute;left:0;top:2251px;width:1200px;height:277px;background:var(--green-2)}
.footer-col{position:absolute;top:46px}
.footer-col h4{font-family:'Raleway',sans-serif;font-weight:500;font-size:14px;color:var(--white);margin-bottom:12px}
.footer-col ul{list-style:none}
.footer-col li{font-size:11px;color:var(--white);line-height:25px}
.footer-rule{position:absolute;left:207px;top:214px;width:800px;height:1px;background:rgba(255,255,255,.7)}
.copyright{position:absolute;left:207px;top:236px;font-size:10px;color:var(--white)}
.social{position:absolute;left:922px;top:230px;display:flex;gap:4px}
.social span{width:28px;height:28px;border-radius:50%;border:1.5px solid var(--white)}
</style>
</head>
<body>

<header class="site-header">
  <div class="brand"><span class="brand-dot"></span><span class="brand-name">SilverYearsQuote</span></div>
  <div class="brand-tag">helping you find the best cover at the best price</div>
  <div class="helpline">
    <div class="helpline-label">Helpline Number</div>
    <div class="helpline-number">
      <svg width="16" height="16" viewBox="0 0 24 24"><path fill="#6aaa1e" d="M6.6 10.8a15.1 15.1 0 0 0 6.6 6.6l2.2-2.2c.3-.3.7-.4 1-.2 1.1.4 2.3.6 3.6.6.6 0 1 .4 1 1V20c0 .6-.4 1-1 1A17 17 0 0 1 3 4c0-.6.4-1 1-1h3.5c.6 0 1 .4 1 1 0 1.3.2 2.5.6 3.6.1.3 0 .7-.2 1z"/></svg>
      0800 731 2946
    </div>
  </div>
</header>

<nav class="main-nav">
  <ul>
    <li class="active">HOME</li><li>CAR</li><li>TRAVEL</li><li>PET</li><li>CARAVAN</li><li>LIFE</li><li>HEALTH</li><li>INCOME PROTECTION</li>
  </ul>
</nav>

<section class="hero">
  <div class="hero-photo" role="img" aria-label="Family jumping hand in hand in a sunlit park under trees"></div>
  <div class="hero-arrow" style="left:162px"></div>
  <div class="hero-arrow" style="left:992px"></div>
  <h1 class="hero-title">BEST PLANS FOR YOU BEST NEEDS</h1>
  <p class="hero-sub">VEHICULA PULVINAR ANTE INTEGER</p>
  <div class="hero-btn">Request a Quote</div>
  <div class="hero-dots"><span></span><span></span><span></span><span></span></div>
  <svg class="hero-curve" width="1200" height="70" viewBox="0 0 1200 70"><path d="M0 70 L0 42 Q600 -30 1200 42 L1200 70 Z" fill="#ffffff"/></svg>
</section>

<h2 class="about-title">About Our Company</h2>
<p class="about-text">A justo id velit placerat molestie Donec dictum lectus non odio Cras a ante vitae enim iaculis aliquam Mauris nunc quam venenatis nec euismod sit amet egestas placerat est Pellentesque habitant morbi tristique senectus et netus et malesuada fames ac turpis egestas Cras id elit Integer quis urna Ut ante enim dapibus malesuada</p>
<div class="btn-outline">Learn More</div>

<div class="carousel-arrow" style="left:162px"></div>
<div class="carousel-arrow" style="left:1004px"></div>
<div class="products">
  <div class="product">
    <svg class="hex" width="207" height="240" viewBox="0 0 207 240"><path d="M103.5 4 L201 60 L201 180 L103.5 236 L6 180 L6 60 Z" fill="#fff" stroke="#dcdcdc" stroke-width="2" stroke-linejoin="round"/></svg>
    <div class="product-icon" role="img" aria-label="House held in hands icon"></div>
    <div class="product-name">Home Insurance</div><div class="product-hint">Click below for more info</div><div class="product-btn">Get a Quote</div>
  </div>
  <div class="product">
    <svg class="hex" width="207" height="240" viewBox="0 0 207 240"><path d="M103.5 4 L201 60 L201 180 L103.5 236 L6 180 L6 60 Z" fill="#fff" stroke="#dcdcdc" stroke-width="2" stroke-linejoin="round"/></svg>
    <div class="product-icon" role="img" aria-label="Damaged car icon"></div>
    <div class="product-name">Car Insurance</div><div class="product-hint">Click below for more info</div><div class="product-btn">Get a Quote</div>
  </div>
  <div class="product">
    <svg class="hex" width="207" height="240" viewBox="0 0 207 240"><path d="M103.5 4 L201 60 L201 180 L103.5 236 L6 180 L6 60 Z" fill="#fff" stroke="#dcdcdc" stroke-width="2" stroke-linejoin="round"/></svg>
    <div class="product-icon" role="img" aria-label="Sailing boat icon"></div>
    <div class="product-name">Travel Insurance</div><div class="product-hint">Click below for more info</div><div class="product-btn">Get a Quote</div>
  </div>
  <div class="product">
    <svg class="hex" width="207" height="240" viewBox="0 0 207 240"><path d="M103.5 4 L201 60 L201 180 L103.5 236 L6 180 L6 60 Z" fill="#fff" stroke="#dcdcdc" stroke-width="2" stroke-linejoin="round"/></svg>
    <div class="product-icon" role="img" aria-label="Paw print icon"></div>
    <div class="product-name">Pet Insurance</div><div class="product-hint">Click below for more info</div><div class="product-btn">Get a Quote</div>
  </div>
</div>

<section class="comparison">
  <h2 class="comparison-title">Comparison Table</h2>
  <table class="compare-table">
    <colgroup><col style="width:140px"><col style="width:95px"><col style="width:95px"><col style="width:110px"><col style="width:110px"><col style="width:100px"><col style="width:80px"></colgroup>
    <thead><tr><th>Company Name</th><th>Cover Amount</th><th>Premium</th><th>Payment Team</th><th>Total Payment</th><th>Intial Period</th><th>Buy Now</th></tr></thead>
    <tbody>
      <tr><td class="provider" style="color:#a8287a">Lumen Mutual</td><td class="amount">£4,200<i class="info">i</i></td><td>£10.00<i class="info">i</i></td><td>40 Years<i class="info">i</i></td><td>£4,800.00<i class="info">i</i></td><td>24 months<i class="info">i</i></td><td class="buycol"><span class="buy">BUY NOW</span><span class="more">MORE INFO</span></td></tr>
      <tr><td class="provider" style="color:#1d3a8a">Northvale</td><td class="amount">£4,200<i class="info">i</i></td><td>£10.00<i class="info">i</i></td><td>40 Years<i class="info">i</i></td><td>£4,800.00<i class="info">i</i></td><td>24 months<i class="info">i</i></td><td class="buycol"><span class="buy">BUY NOW</span><span class="more">MORE INFO</span></td></tr>
      <tr><td class="provider" style="color:#1f3f8f">Crestline</td><td class="amount">£3,000<i class="info">i</i></td><td>£10.00<i class="info">i</i></td><td>20 Years<i class="info">i</i></td><td>£4,800.00<i class="info">i</i></td><td>24 months<i class="info">i</i></td><td class="buycol"><span class="buy">BUY NOW</span><span class="more">MORE INFO</span></td></tr>
      <tr><td class="provider" style="color:#1b3d7a">Harbour Life</td><td class="amount">£2,200<i class="info">i</i></td><td>£10.00<i class="info">i</i></td><td>30 Years<i class="info">i</i></td><td>£4,800.00<i class="info">i</i></td><td>24 months<i class="info">i</i></td><td class="buycol"><span class="buy">BUY NOW</span><span class="more">MORE INFO</span></td></tr>
      <tr><td class="provider" style="color:#2a2a5a">Kestrel Cover</td><td class="amount">£2,900<i class="info">i</i></td><td>£10.00<i class="info">i</i></td><td>30 Years<i class="info">i</i></td><td>£4,800.00<i class="info">i</i></td><td>24 months<i class="info">i</i></td><td class="buycol"><span class="buy">BUY NOW</span><span class="more">MORE INFO</span></td></tr>
      <tr><td class="provider" style="color:#1e5aa0">Alder &amp; Co</td><td class="amount">£2,600<i class="info">i</i></td><td>£10.00<i class="info">i</i></td><td>20 Years<i class="info">i</i></td><td>£4,800.00<i class="info">i</i></td><td>24 months<i class="info">i</i></td><td class="buycol"><span class="buy">BUY NOW</span><span class="more">MORE INFO</span></td></tr>
      <tr><td class="provider" style="color:#1c3c86">Meridian</td><td class="amount">£22,00<i class="info">i</i></td><td>£10.00<i class="info">i</i></td><td>15 Years<i class="info">i</i></td><td>£4,800.00<i class="info">i</i></td><td>24 months<i class="info">i</i></td><td class="buycol"><span class="buy">BUY NOW</span><span class="more">MORE INFO</span></td></tr>
      <tr><td class="provider" style="color:#1a4d8c">Beacon</td><td class="amount">£2,100<i class="info">i</i></td><td>£10.00<i class="info">i</i></td><td>10 Years<i class="info">i</i></td><td>£4,800.00<i class="info">i</i></td><td>24 months<i class="info">i</i></td><td class="buycol"><span class="buy">BUY NOW</span><span class="more">MORE INFO</span></td></tr>
    </tbody>
  </table>
</section>

<section class="club">
  <div class="club-photo" role="img" aria-label="Desk from above with laptop, keyboard, camera, phone and coffee cup in greyscale"></div>
  <h2 class="club-title">Join the Club</h2>
  <p class="club-text">Aenean porttitor eros vel dolor Donec convallis pede venenatis nibh Duis quam Nam eget lacus Aliquam erat volutpat Quisque dignissim congue</p>
  <div class="signup"><span class="signup-field">Email address</span><span class="signup-btn">SIGN UP</span></div>
</section>

<footer class="site-footer">
  <div class="footer-col" style="left:207px"><h4>COMPANY</h4><ul><li>Home</li><li>About Us</li><li>Contact Us</li><li>Career Opportunities</li></ul></div>
  <div class="footer-col" style="left:393px"><h4>SERVICES</h4><ul><li>Home Insurance</li><li>Pet Insurance</li><li>Car Insurance</li><li>Life Insurance</li></ul></div>
  <div class="footer-col" style="left:519px;top:80px"><ul><li>Travel Insurance</li><li>Income Protection</li><li>Caravan Protection</li></ul></div>
  <div class="footer-col" style="left:691px;top:50px"><h4>RESOURCES</h4><ul><li>Support</li><li>FAQ</li><li>Privacy Policy</li><li>Contact Us</li></ul></div>
  <div class="footer-col" style="left:846px"><h4>WHY US</h4><ul><li>Silver Years HQ</li><li>14 Orchard Lane</li><li>Bristol BS1 4DJ</li><li>United Kingdom</li></ul></div>
  <div class="footer-rule"></div>
  <div class="copyright">© 2016 Company Name. All right reserved. Term of Use</div>
  <div class="social"><span></span><span></span><span></span><span></span></div>
</footer>

</body>
</html>
```